New business card for a regional office of a US M&A company

We need business card for a finance company, office based in Hong Kong , our Head office is in US, our business is to Merge and acquires companies , the new office will be a regional office for the Asia Pacific region. We want to use the head office logo as attached ( but don't have to be exactly the same, can be a variation to it) as a base and then add Asia Pacific alongside the logo.
We would prefer to have be bilingual Eng + Chinese, although we don't really have Chinese company name .

Industry/Entity Type

Business

Contact Information for Business Card

Carla Beth Soren
 

VP,
APAC M&A Operations
TOVAR CREST Asia Pacific Limited
 
Unit 1407, K82
27 Sai Lok Fung Road, 
Hong Kong 
 
M: +852 6481 2037
T : +852 2736 4100
F : +852 2736 4155
VOIP: 4813
 
cbsoren@tovarcrest.com

Font styles to use
Serif
Sans Serif

Colors

Designer to choose colors to be used in the design.

Requirements
Must have
• APAC Office

```html
<!DOCTYPE html>
<html lang="en">
<head>
<meta charset="utf-8">
<title>Tovar Crest Business Card</title>
<link rel="stylesheet" href="https://fonts.googleapis.com/css2?family=Open+Sans:wght@400;600;800&display=swap">
<style>
  :root {
    --stage: #7b7880;
    --navy: #0c2a47;
    --navy-deep: #0b2540;
    --navy-soft: #143a5e;
    --cyan: #1f9fcf;
    --white: #ffffff;
    --mark: #e9edf1;
  }
  * { box-sizing: border-box; margin: 0; padding: 0; }
  html, body {
    width: 1200px;
    height: 675px;
    overflow: hidden;
    background: var(--stage);
    font-family: "Open Sans", Arial, sans-serif;
  }
  .stage {
    width: 1200px;
    height: 675px;
    display: flex;
    align-items: center;
    justify-content: center;
    gap: 40px;
  }
  .card {
    position: relative;
    width: 540px;
    height: 308px;
    overflow: hidden;
    box-shadow: 0 6px 18px rgba(0,0,0,0.28);
  }
  /* Front */
  .card-front { background: var(--navy); }
  .front-texture {
    position: absolute;
    inset: 0;
    background: linear-gradient(135deg, var(--navy-soft) 0%, var(--navy) 55%, var(--navy-deep) 100%);
  }
  .front-brand {
    position: absolute;
    inset: 0;
    display: flex;
    flex-direction: column;
    align-items: center;
    justify-content: center;
    gap: 18px;
  }
  .brand-square {
    width: 58px;
    height: 58px;
    background: var(--mark);
  }
  .brand-name {
    color: var(--cyan);
    font-weight: 800;
    letter-spacing: 1px;
    line-height: 1;
  }
  .front-brand .brand-name { font-size: 46px; }
  /* Back */
  .card-back { background: var(--navy-deep); color: var(--white); }
  .back-brand {
    position: absolute;
    top: 52px;
    right: 44px;
    display: flex;
    flex-direction: column;
    align-items: center;
    gap: 10px;
  }
  .back-brand .brand-square { width: 30px; height: 30px; }
  .back-brand .brand-name { font-size: 24px; }
  .contact {
    position: absolute;
    left: 44px;
    top: 48px;
  }
  .contact-name {
    font-size: 19px;
    font-weight: 400;
    margin-bottom: 14px;
  }
  .contact-block {
    font-size: 9.5px;
    line-height: 1.45;
    margin-bottom: 20px;
  }
  .contact-block:last-child { margin-bottom: 0; }
</style>
</head>
<body>
<main class="stage">
  <section class="card card-front" aria-label="Card front">
    <div class="front-texture" role="img" aria-label="Repeating diamond pattern in tones of navy blue"></div>
    <div class="front-brand">
      <span class="brand-square"></span>
      <span class="brand-name">TOVAR CREST</span>
    </div>
  </section>

  <section class="card card-back" aria-label="Card back">
    <div class="contact">
      <h1 class="contact-name">Carla Beth Soren</h1>
      <p class="contact-block">
        VP,<br>
        APAC M&amp;A Operations<br>
        Tovar Crest Asia Pacific Limited
      </p>
      <p class="contact-block">
        Unit 1407, K82<br>
        27 Sai Lok Fung Road,<br>
        Hong Kong
      </p>
      <p class="contact-block">
        M: +852 6481 2037<br>
        T : +852 2736 4100<br>
        F : +852 2736 4155<br>
        VOIP: 4813
      </p>
      <p class="contact-block">cbsoren@tovarcrest.com</p>
    </div>
    <div class="back-brand">
      <span class="brand-square"></span>
      <span class="brand-name">TOVAR CREST</span>
    </div>
  </section>
</main>
</body>
</html>
```